Upsell Vertical Banner Ad Design For B2B Marketing Agency Vertical 768px × 1180px IS THE SIZE

I need a banner made for my website www.brightlanepromotionhub.biz This banner will be an upsell advertisement for after someone signs up for my monthly program. When they login to their account for the 1st time I will give them the chance to upgrade their account to our annual program with just one click.

this is a page that upsells it currently to give you an idea how we market ourselves:
https://tlpx.pagevault-example.com/page/tlp-annual-upsell

Use this content:

Are You Ready To Commit To Taking Your Business To The Next Level?

Because We're In This For The Long-Haul and Dedicated To Your Success...

Save $300 By Upgrading To An Annual Membership And Pay Only $74/mth

((BUTTON))Yes, Upgrade My Plan Right Now!

*Must prepay the full year at only $898/yr!

Target Market(s)

business owners

Industry/Entity Type

Marketing

Requirements
Must have
• 768px × 1180px IS THE SIZE vertical

Use this content:

Nice to have
• Use this content:

Should not have
• Use this content:

```html
<!DOCTYPE html>
<html lang="en">
<head>
<meta charset="utf-8">
<title>Bright Lane Promotion Hub – Annual Upgrade Banner</title>
<link href="https://fonts.googleapis.com/css2?family=Lato:ital,wght@0,300;0,400;0,700;0,900;1,400&display=swap" rel="stylesheet">
<style>
  :root {
    --stage: #b3b3b3;
    --paper: #ffffff;
    --brand-blue: #1f78c1;
    --panel-blue: #1877c6;
    --ink-grey: #4a4a4a;
    --red-top: #e8222a;
    --red-bottom: #9c0f14;
    --night: #131d27;
    --button-red: #d8151c;
    --white: #ffffff;
    --hero-warm: #c43a3f;
    --hero-mid: #3a82c8;
    --hero-skin: #d19a78;
  }
  * { box-sizing: border-box; margin: 0; padding: 0; }
  html, body { width: 1004px; height: 1200px; overflow: hidden; }
  body { background: var(--stage); font-family: "Lato", sans-serif; position: relative; }

  .banner {
    position: absolute; left: 173px; top: 70px;
    width: 678px; height: 1041px;
    background: var(--paper); overflow: hidden;
  }

  .brand {
    position: absolute; top: 22px; left: 0; width: 100%;
    display: flex; justify-content: center; align-items: center; gap: 12px;
  }
  .brand__mark { width: 30px; height: 30px; background: var(--brand-blue); }
  .brand__name {
    font-weight: 700; font-size: 29px; color: var(--brand-blue);
    letter-spacing: 0.5px; line-height: 1;
  }

  .hero-photo {
    position: absolute; top: 91px; left: 0; width: 678px; height: 365px;
    background: linear-gradient(100deg, var(--hero-warm) 0%, var(--hero-mid) 55%, var(--hero-skin) 100%);
  }

  .headline-pre {
    position: absolute; top: 268px; left: 41px;
    font-weight: 400; font-size: 54px; color: var(--white);
    line-height: 1; letter-spacing: -0.5px;
  }
  .headline-main {
    position: absolute; top: 306px; left: 38px;
    font-weight: 900; font-size: 180px; color: var(--white);
    line-height: 1; letter-spacing: 5px;
    text-shadow: 0 3px 4px rgba(0,0,0,0.12);
  }

  .subhead {
    position: absolute; top: 468px; left: 0; width: 100%;
    text-align: center; font-weight: 400; font-size: 38px;
    line-height: 37px; color: var(--ink-grey); letter-spacing: -0.3px;
  }
  .subhead__accent { color: var(--brand-blue); font-weight: 900; }

  .lower-bands { position: absolute; top: 557px; left: 0; width: 678px; height: 484px; }

  .pitch { position: absolute; top: 690px; left: 0; width: 100%; text-align: center; color: var(--white); }
  .pitch__lead { font-weight: 400; font-size: 27px; line-height: 34px; }
  .pitch__big {
    font-weight: 900; font-size: 69px; line-height: 68px;
    letter-spacing: -1px; margin-top: 4px;
  }
  .pitch__rule { width: 510px; height: 3px; background: var(--white); margin: 8px auto 6px; }
  .pitch__offer { font-weight: 400; font-size: 25px; line-height: 30px; }
  .pitch__offer strong { font-weight: 900; }

  .cta {
    position: absolute; top: 945px; left: 79px; width: 515px; height: 54px;
    background: linear-gradient(180deg, #ea2a2f 0%, var(--button-red) 100%);
    border: 2px solid var(--white); border-radius: 7px;
    display: flex; align-items: center; justify-content: center; gap: 16px;
    color: var(--white); font-weight: 900; font-size: 25px; text-decoration: none;
  }
  .cta__tick { width: 32px; height: 32px; }

  .footnote {
    position: absolute; top: 1008px; left: 0; width: 100%;
    text-align: center; font-style: italic; font-size: 17px; color: var(--white);
  }
  .pointer-icon { position: absolute; top: 974px; left: 606px; width: 50px; height: 50px; }
</style>
</head>
<body>
  <main class="banner">
    <header class="brand">
      <span class="brand__mark"></span>
      <span class="brand__name">BRIGHT LANE PROMOTION HUB</span>
    </header>

    <div class="hero-photo" role="img" aria-label="Photo: hand holding a glossy sphere with rising arrows, colourful growth arrows behind"></div>

    <p class="headline-pre">ARE YOU</p>
    <h1 class="headline-main">READY</h1>

    <p class="subhead">TO COMMIT TO TAKING YOUR<br>BUSINESSES TO <span class="subhead__accent">THE NEXT LEVEL</span>?</p>

    <svg class="lower-bands" viewBox="0 0 678 484" aria-hidden="true">
      <defs>
        <linearGradient id="redBand" x1="0" y1="0" x2="0" y2="1">
          <stop offset="0" stop-color="#e8222a"/>
          <stop offset="1" stop-color="#9c0f14"/>
        </linearGradient>
      </defs>
      <polygon points="0,76 339,0 678,76 678,146 339,69 0,146" fill="url(#redBand)"/>
      <polygon points="0,146 339,69 678,146 678,360 0,360" fill="#1877c6"/>
      <rect x="0" y="360" width="678" height="124" fill="#131d27"/>
      <polygon points="325,360 339,374 353,360" fill="#1877c6"/>
    </svg>

    <section class="pitch">
      <p class="pitch__lead">BECAUSE WE’RE IN THIS<br>FOR THE LONG-HAUL &amp; DEDICTED TO</p>
      <p class="pitch__big">YOUR SUCCESS!</p>
      <div class="pitch__rule"></div>
      <p class="pitch__offer"><strong>Save $300</strong> By Upgrading To An Annual Membership<br>And Pay Only $74/mth</p>
    </section>

    <a class="cta" href="https://tlpx.pagevault-example.com/page/tlp-annual-upsell">
      <svg class="cta__tick" viewBox="0 0 32 32" aria-hidden="true">
        <rect x="3" y="7" width="22" height="22" fill="none" stroke="#fff" stroke-width="3"/>
        <path d="M8 17 L14 24 L29 3" fill="none" stroke="#fff" stroke-width="4" stroke-linecap="round" stroke-linejoin="round"/>
      </svg>
      <span>YES, UPGRADE MY PLAN RIGHT NOW!</span>
    </a>

    <p class="footnote">*Must prepay the full year at only $898/yr!</p>

    <svg class="pointer-icon" viewBox="0 0 50 50" aria-hidden="true">
      <g stroke="#fff" stroke-width="3" stroke-linecap="round">
        <line x1="14" y1="3" x2="14" y2="9"/>
        <line x1="3" y1="14" x2="9" y2="14"/>
        <line x1="6" y1="6" x2="10" y2="10"/>
        <line x1="22" y1="6" x2="19" y2="10"/>
        <line x1="6" y1="22" x2="10" y2="19"/>
      </g>
      <path d="M16 16 L16 40 L22 34 L27 45 L32 43 L27 32 L35 32 Z" fill="#fff"/>
    </svg>
  </main>
</body>
</html>
```